Medical Practice Business Card

we need a business card for our new medical ophthalmology practice based in Needham Massachusetts. we are looking for a simple , modern and elegant design.
the card needs to contain the following
1- the logo of our practice (please see attached file)
2- the name of the practice : "Silver Birch Retina Care"
3- Doctor's Name: Tobias Rendell MD PhD
4- Specialty: Board-Certified Vitreoretinal Surgeon
5- practice address: 87 Larkspur Ave, Suite 210, Larchmere XY 00481
7- Office number: 617- 482 - 7730
8- fax number: 617- 391 - 2268
9- email: info@sbretinahub.example
10- website: www.sbretinahub.example

```html
<!DOCTYPE html>
<html lang="en">
<head>
<meta charset="utf-8">
<title>Silver Birch Retina Care – Business Card</title>
<link href="https://fonts.googleapis.com/css2?family=Raleway:ital,wght@0,400;0,500;0,600;0,700;1,400&display=swap" rel="stylesheet">
<style>
  :root {
    --stage: #009ed8;
    --card: #f7f8f9;
    --navy: #1b3a5c;
    --blue-deep: #1b88b8;
    --blue-mid: #159fd6;
    --blue: #22b0e6;
    --blue-light: #3fc3ef;
    --blue-pale: #45c4f0;
    --ink: #2c2f33;
    --white: #ffffff;
  }
  * { box-sizing: border-box; margin: 0; padding: 0; }
  html, body { width: 1200px; height: 1200px; overflow: hidden; }
  body {
    background: var(--stage);
    font-family: "Raleway", sans-serif;
    position: relative;
  }
  .card {
    position: absolute;
    width: 730px;
    height: 446px;
    background: var(--card);
    overflow: hidden;
    box-shadow: 0 2px 6px rgba(0, 40, 70, 0.18);
  }
  .card--front { left: 238px; top: 78px; border-radius: 60px 0 60px 0; }
  .card--back  { left: 235px; top: 617px; border-radius: 0 60px 0 60px; }

  /* front header */
  .header { position: absolute; top: 61px; left: 0; height: 71px; width: 100%; display: flex; }
  .header .seg { height: 100%; }
  .seg--navy { background: var(--navy); width: 89px; }
  .seg--deep { background: var(--blue-deep); width: 99px; }
  .seg--mid { background: var(--blue-mid); width: 106px; }
  .seg--blue { background: var(--blue); width: 84px; }
  .name-band {
    flex: 1; background: var(--blue-light);
    display: flex; align-items: center; padding-left: 19px;
    color: var(--white);
  }
  .doctor-name { font-size: 31px; font-weight: 700; letter-spacing: 0.2px; }
  .doctor-title { font-size: 20px; font-style: italic; font-weight: 400; margin-left: 8px; opacity: 0.9; }
  .specialty-band {
    position: absolute; top: 134px; left: 378px; right: 0; height: 30px;
    background: var(--blue-pale); color: var(--white);
    font-size: 16px; font-weight: 500; padding-left: 19px;
    display: flex; align-items: center;
  }

  /* practice name */
  .practice { position: absolute; display: flex; align-items: center; color: var(--navy); font-weight: 600; }
  .practice__dot { border-radius: 50%; background: var(--blue-light); flex: none; }
  .practice__name { line-height: 1.05; letter-spacing: 1px; text-transform: uppercase; }
  .practice--small { left: 84px; top: 212px; }
  .practice--small .practice__dot { width: 13px; height: 13px; margin-right: 13px; }
  .practice--small .practice__name { font-size: 26px; }
  .practice--large { left: 0; right: 0; top: 128px; justify-content: center; }
  .practice--large .practice__dot { width: 24px; height: 24px; margin-right: 24px; }
  .practice--large .practice__name { font-size: 52px; }

  /* contacts */
  .contacts { position: absolute; left: 426px; top: 190px; list-style: none; }
  .contact { display: flex; align-items: center; height: 30px; margin-bottom: 13px; color: var(--ink); font-size: 15px; line-height: 1.45; }
  .contact--address { height: 40px; margin-bottom: 10px; }
  .contact svg { width: 30px; height: 30px; flex: none; margin-right: 30px; fill: var(--blue-mid); }

  /* dashes */
  .dashes { position: absolute; display: flex; gap: 7px; }
  .dashes span { width: 18px; height: 5px; }
  .dashes span:nth-child(1) { background: var(--blue-light); }
  .dashes span:nth-child(2) { background: var(--blue); }
  .dashes span:nth-child(3) { background: var(--blue-mid); }
  .dashes span:nth-child(4) { background: var(--blue-deep); }
  .dashes span:nth-child(5) { background: var(--navy); }
  .card--front .dashes { left: 83px; top: 406px; }
  .card--back .dashes { left: 100px; top: 412px; }

  .footer-band { position: absolute; left: 0; top: 415px; width: 392px; height: 31px; background: var(--blue-deep); }

  /* back footer */
  .back-footer { position: absolute; top: 353px; left: 0; width: 100%; height: 40px; display: flex; }
  .back-footer .seg { height: 100%; width: 92px; }
  .back-footer .seg--l1 { background: var(--blue-light); }
  .back-footer .seg--l2 { background: var(--blue); }
  .back-footer .seg--l3 { background: var(--blue-mid); }
  .back-footer .seg--l4 { background: var(--blue-deep); width: 136px; }
  .back-footer .url-band {
    flex: 1; background: var(--navy); color: var(--white);
    display: flex; align-items: center; justify-content: center;
    font-size: 16px; font-weight: 500; border-left: 2px solid var(--white);
  }
</style>
</head>
<body>

<section class="card card--front" aria-label="Business card front">
  <div class="header">
    <div class="seg seg--navy"></div>
    <div class="seg seg--deep"></div>
    <div class="seg seg--mid"></div>
    <div class="seg seg--blue"></div>
    <div class="name-band">
      <span class="doctor-name">Tobias Rendell</span>
      <span class="doctor-title">MD PhD</span>
    </div>
  </div>
  <div class="specialty-band">Board-Certified Vitreoretinal Surgeon</div>

  <div class="practice practice--small">
    <span class="practice__dot"></span>
    <span class="practice__name">Silver Birch<br>Retina Care</span>
  </div>

  <ul class="contacts">
    <li class="contact contact--address">
      <svg viewBox="0 0 24 24" aria-hidden="true"><path d="M12 2 1 12h3v10h6v-6h4v6h6V12h3z"/></svg>
      <span>87 Larkspur Ave, Suite 210,<br>Larchmere XY 00481</span>
    </li>
    <li class="contact">
      <svg viewBox="0 0 24 24" aria-hidden="true"><circle cx="12" cy="12" r="11"/><path fill="#fff" d="M8.2 6.5l2 2.3-1.2 1.4c.8 1.8 2.2 3.3 4 4.1l1.4-1.2 2.3 2-1.3 2c-4.5-.5-8.4-4.4-8.9-8.9z"/></svg>
      <span>617- 482 - 7730</span>
    </li>
    <li class="contact">
      <svg viewBox="0 0 24 24" aria-hidden="true"><path d="M6 2h12v6H6zM3 9h18a1 1 0 0 1 1 1v8h-4v-4H6v4H2v-8a1 1 0 0 1 1-1zM7 15h10v7H7z"/></svg>
      <span>617- 391 - 2268</span>
    </li>
    <li class="contact">
      <svg viewBox="0 0 24 24" aria-hidden="true"><path d="M5 1h10l5 5v17H5z"/><path fill="#fff" d="M8 9h9v1.3H8zM8 12h9v1.3H8zM8 15h9v1.3H8zM8 18h6v1.3H8z"/></svg>
      <span>info@sbretinahub.example</span>
    </li>
    <li class="contact">
      <svg viewBox="0 0 24 24" aria-hidden="true"><circle cx="12" cy="12" r="11"/><path fill="none" stroke="#fff" stroke-width="1.4" d="M1 12h22M12 1c-4 4-4 18 0 22M12 1c4 4 4 18 0 22M3 6.5h18M3 17.5h18"/></svg>
      <span>www.sbretinahub.example</span>
    </li>
  </ul>

  <div class="dashes"><span></span><span></span><span></span><span></span><span></span></div>
  <div class="footer-band"></div>
</section>

<section class="card card--back" aria-label="Business card back">
  <div class="practice practice--large">
    <span class="practice__dot"></span>
    <span class="practice__name">Silver Birch<br>Retina Care</span>
  </div>
  <div class="back-footer">
    <div class="seg seg--l1"></div>
    <div class="seg seg--l2"></div>
    <div class="seg seg--l3"></div>
    <div class="seg seg--l4"></div>
    <div class="url-band">www.sbretinahub.example</div>
  </div>
  <div class="dashes"><span></span><span></span><span></span><span></span><span></span></div>
</section>

</body>
</html>
```